Summit & Compass Flyer

2023 Summit & Compass
Military, Veterans, Law Enforcement & Fire Fighters
Receive $300* Off Purchased Materials
*$300 maximum discount per order. $3,000 order minimum. Redeem up to 3 times per year.
Terms & Conditions: This program is intended for the professional contractor that supports Ridgewren Supply with material purchases. One-time purchasers and institutions are not eligible for this program. By choosing to participate, you represent to Ridgewren Supply that your participation is not prohibited by law. Ridgewren Supply reserves the right to cancel, suspend, and/or modify this promotion at any time, for any reason, without prior notice. Employees at Ridgewren Supply are not eligible to participate. All rights reserved by Ridgewren Supply. Promotion expires December 31, 2023.
Please use our 2023 logo - attached
I'm also attaching the 2022 flyer as an example but looking for a refreshed design!

```html
<!DOCTYPE html>
<html lang="en">
<head>
<meta charset="utf-8">
<title>Summit &amp; Compass Flyer</title>
<link href="https://fonts.googleapis.com/css2?family=Montserrat:wght@400;500;600;700;800;900&display=swap" rel="stylesheet">
<style>
  :root {
    --navy: #2b3278;
    --navy-deep: #1f2566;
    --blue: #0a9be0;
    --blue-light: #2bb3f0;
    --grey-text: #555a60;
    --amp-grey: #6b6e73;
    --paper: #f6f6f7;
    --white: #ffffff;
  }
  * { box-sizing: border-box; margin: 0; padding: 0; }
  html, body { width: 922px; height: 1200px; overflow: hidden; }
  body { background: var(--white); font-family: 'Montserrat', sans-serif; }

  .flyer {
    position: relative;
    width: 922px;
    height: 1200px;
    background: linear-gradient(160deg, #fbfbfc 0%, var(--paper) 45%, #fdfdfd 100%);
    overflow: hidden;
  }

  .brand-mark {
    position: absolute;
    top: 130px;
    left: 0;
    width: 100%;
    display: flex;
    justify-content: center;
    align-items: center;
    gap: 18px;
  }
  .brand-mark__dot {
    width: 58px; height: 58px;
    border-radius: 50%;
    background: var(--navy);
  }
  .brand-mark__name {
    font-weight: 700;
    font-size: 44px;
    color: var(--navy);
    letter-spacing: 0.5px;
  }

  .headline {
    position: absolute;
    top: 292px;
    left: 0; width: 100%;
    text-align: center;
    font-weight: 800;
    font-size: 118px;
    line-height: 1;
    letter-spacing: -2px;
  }
  .headline__amount {
    background: linear-gradient(180deg, #4a53a8 0%, var(--navy-deep) 100%);
    -webkit-background-clip: text; background-clip: text; color: transparent;
  }
  .headline__off {
    background: linear-gradient(180deg, var(--blue-light) 0%, #0788cc 100%);
    -webkit-background-clip: text; background-clip: text; color: transparent;
  }

  .program-title {
    position: absolute;
    top: 428px;
    left: 0; width: 100%;
    text-align: center;
    font-weight: 800;
    font-size: 48px;
    color: var(--blue);
    text-transform: uppercase;
    letter-spacing: 0.3px;
  }
  .program-title__amp { color: var(--amp-grey); }

  .audience {
    position: absolute;
    top: 492px;
    left: 0; width: 100%;
    text-align: center;
    font-weight: 600;
    font-size: 24px;
    color: var(--grey-text);
  }

  .hero-strip {
    position: absolute;
    top: 562px;
    left: 0;
    width: 922px;
    height: 294px;
    display: block;
  }

  .offer-band {
    position: absolute;
    top: 856px;
    left: 0;
    width: 922px;
    height: 146px;
    background: var(--blue);
    display: grid;
    grid-template-columns: 292px 1fr 330px;
    align-items: center;
    color: var(--white);
    text-align: center;
  }
  .offer-band__col { padding: 0 10px; }
  .offer-band__col + .offer-band__col { border-left: 2px solid var(--white); height: 100px; display: flex; flex-direction: column; justify-content: center; }
  .offer-band__col:first-child { height: 100px; display: flex; flex-direction: column; justify-content: center; }
  .offer-band__small { font-size: 19px; font-weight: 500; line-height: 1.2; }
  .offer-band__big { font-size: 40px; font-weight: 800; line-height: 1.1; }
  .offer-band__mid { font-size: 27px; font-weight: 500; line-height: 1.3; }
  .offer-band__mid strong { font-weight: 800; }
  .offer-band__note { font-size: 21px; font-weight: 500; line-height: 1.25; }
  .offer-band__note strong { font-weight: 800; font-size: 26px; }
  .offer-band__note .min { font-weight: 800; }

  .terms {
    position: absolute;
    top: 1002px;
    left: 0;
    width: 922px;
    height: 136px;
    background: var(--navy);
    color: var(--white);
    font-size: 12.3px;
    font-weight: 500;
    line-height: 1.42;
    text-align: center;
    padding: 26px 52px 0;
  }

  .footer {
    position: absolute;
    top: 1138px;
    left: 0;
    width: 922px;
    height: 62px;
    background: var(--white);
    display: flex;
    justify-content: space-between;
    align-items: center;
    padding: 0 34px 0 54px;
    font-size: 19px;
    color: var(--grey-text);
  }
  .footer__site strong { color: var(--navy); font-weight: 700; }
  .footer__social { display: flex; align-items: center; gap: 10px; }
  .footer__social-dot { width: 24px; height: 24px; border-radius: 50%; background: var(--navy); }
  .footer__handle { font-weight: 500; color: var(--navy); }
</style>
</head>
<body>
<main class="flyer">

  <div class="brand-mark">
    <span class="brand-mark__dot"></span>
    <span class="brand-mark__name">Ridgewren Supply</span>
  </div>

  <h1 class="headline"><span class="headline__amount">$300</span> <span class="headline__off">OFF*</span></h1>

  <h2 class="program-title">Summit <span class="program-title__amp">&amp;</span> Compass 2023</h2>

  <p class="audience">Military, Veterans, Law Enforcement &amp; Fire Fighters</p>

  <svg class="hero-strip" viewBox="0 0 922 294" role="img" aria-label="Photo strip of four slanted panels: a military family with children holding a flag, a veteran soldier in a helmet before a flag, a police officer, and a firefighter in turnout gear">
    <defs>
      <linearGradient id="panel-family" x1="0" y1="0" x2="0" y2="1">
        <stop offset="0" stop-color="#4f7f3a"/>
        <stop offset="1" stop-color="#8aa66a"/>
      </linearGradient>
      <linearGradient id="panel-veteran" x1="0" y1="0" x2="0" y2="1">
        <stop offset="0" stop-color="#9a6a5e"/>
        <stop offset="1" stop-color="#7d6a55"/>
      </linearGradient>
      <linearGradient id="panel-police" x1="0" y1="0" x2="0" y2="1">
        <stop offset="0" stop-color="#8a8f93"/>
        <stop offset="1" stop-color="#2a2c30"/>
      </linearGradient>
      <linearGradient id="panel-fire" x1="0" y1="0" x2="0" y2="1">
        <stop offset="0" stop-color="#a7794f"/>
        <stop offset="1" stop-color="#3b3330"/>
      </linearGradient>
    </defs>
    <polygon points="0,0 270,0 200,294 0,294" fill="url(#panel-family)"/>
    <polygon points="274,0 498,0 428,294 204,294" fill="url(#panel-veteran)"/>
    <polygon points="502,0 712,0 642,294 432,294" fill="url(#panel-police)"/>
    <polygon points="716,0 922,0 922,294 646,294" fill="url(#panel-fire)"/>
    <polygon points="0,0 50,0 0,120" fill="var(--navy)"/>
    <polygon points="922,60 922,294 868,294" fill="var(--navy)"/>
  </svg>

  <section class="offer-band">
    <div class="offer-band__col">
      <span class="offer-band__small">Receive</span>
      <span class="offer-band__big">$300*OFF</span>
      <span class="offer-band__small">Purchased Materials</span>
    </div>
    <div class="offer-band__col">
      <span class="offer-band__mid"><strong>Redeem</strong> up to</span>
      <span class="offer-band__mid"><strong>3 times</strong> per year</span>
    </div>
    <div class="offer-band__col">
      <span class="offer-band__note"><strong>*$300</strong></span>
      <span class="offer-band__note">maximum discount</span>
      <span class="offer-band__note">per order.</span>
      <span class="offer-band__note min">$3,000 order minimum.</span>
    </div>
  </section>

  <p class="terms">Terms &amp; Conditions: This program is intended for the professional contractor that supports Ridgewren Supply with material purchases. One-time purchasers and institutions are not eligible for this program. By choosing to participate, you represent to Ridgewren Supply that your participation is not prohibited by law. Ridgewren Supply reserves the right to cancel, suspend, and/or modify this promotion at any time, for any reason, without prior notice. Employees at Ridgewren Supply are not eligible to participate. All rights reserved by Ridgewren Supply. Promotion expires December 31, 2023.</p>

  <footer class="footer">
    <span class="footer__site">www.<strong>ridgewrensupply</strong>.com</span>
    <span class="footer__social">
      <span class="footer__social-dot"></span>
      <span class="footer__handle">@ridgewrenSupply</span>
    </span>
  </footer>

</main>
</body>
</html>
```